Tress Radiant from root to soul. Hair stylist that specializes in extensions.

I am Marisol I am a hair stylist and I would like a website designed for my hair business.

I currently book clients via my profile on glamslot.net/marisolbreck

I need a professional website ( tressradiantfromroottosoul.net ) to display photos and prices for services offered.

I would like to have a home page with a brief bio, Image with logo and testimonials at the bottom, and a header with tab that include: menu of services, gallery,and FAQs.

On the "Services" page, I'm not interested in photos on this page. Just the name of the service, brief description, and pricing. I would also like to have, on this page, "Appointment Request" with fields that include: Name, service requested, desired time frame (morning, afternoon, evening), and contact number and email

On the "Gallery" page, I would like pictures only, but arranged and/or presented in a creative way...

Target Market(s)

Women ages 25-55 who interested in hair extension services.

Industry/Entity Type

Hair And Beauty

Coding

Coded - Design and coding required

Number of Pages Required

5+ page

Font styles to use
Sans Serif

Requirements
Must have
• Must include tabs that include, Menu of services offered, a quik pae link to pay deposits with ease, location, contact information, photo gallery, and policy/faqs.
Nice to have
• If possible i would like to stream music with the ability to be silenced. I would like a neutral color palette tans and beige.
Should not have
• stock images

```html
<!DOCTYPE html>
<html lang="en">
<head>
<meta charset="utf-8">
<title>Tress Radiant from root to soul</title>
<link href="https://fonts.googleapis.com/css2?family=Cinzel:wght@400;600;700&family=Open+Sans:ital,wght@0,400;0,600;0,700;1,400;1,600&display=swap" rel="stylesheet">
<style>
:root{
  --white:#ffffff;
  --ink:#2b2623;
  --body:#5a5350;
  --accent:#d6a17e;
  --rose:#c9aa9c;
  --rose-deep:#b89384;
  --footer:#d9bfb3;
  --cream:#f3f1ec;
  --soft:#f7f6f4;
  --line:#d8d3cf;
  --teal:#3cc5bd;
  --heart:#c0392b;
  --header:rgba(70,62,58,.72);
}
*{box-sizing:border-box;margin:0;padding:0}
html,body{width:1200px;height:2609px;overflow:hidden;background:var(--white)}
body{position:relative;font-family:"Open Sans",sans-serif;color:var(--body)}
.abs{position:absolute}

/* hero */
.hero{left:0;top:0;width:1200px;height:548px;background:linear-gradient(180deg,#e7e2dc 0%,#c9b7a6 40%,#8c6f58 70%,#d8cdc3 100%)}
.hero-photo{left:0;top:0;width:1200px;height:548px;background:radial-gradient(ellipse 360px 420px at 600px 270px,#e8d2c2 0%,#b58e72 45%,rgba(90,62,42,0) 80%)}
.topbar{left:0;top:0;width:1200px;height:108px;background:var(--header);border-top:4px solid var(--accent)}
.brand{left:90px;top:30px;width:190px;color:var(--white);font-family:"Cinzel",serif;font-weight:700;font-size:19px;line-height:22px;letter-spacing:1px}
.brand small{font-size:11px;font-weight:600}
.phone{left:760px;top:20px;display:flex;align-items:center;gap:12px;color:var(--white);font-family:"Cinzel",serif;font-size:21px}
.login{left:944px;top:20px;display:flex;align-items:center;gap:10px;color:var(--white);font-family:"Cinzel",serif;font-size:14px}
.nav{right:96px;top:70px;display:flex;gap:18px;color:var(--white);font-family:"Cinzel",serif;font-size:15px}
.hero-title{left:0;top:250px;width:1200px;text-align:center;color:var(--white);font-family:"Cinzel",serif;font-weight:400;font-size:59px;letter-spacing:4px;line-height:66px}
.hero-sub{left:0;top:316px;width:1200px;text-align:center;color:var(--white);font-family:"Cinzel",serif;font-size:29px;letter-spacing:3px}
.arrow{top:358px}
.tagline{top:488px;width:300px;text-align:center;color:var(--white);font-family:"Cinzel",serif;font-size:24px;letter-spacing:3px;text-shadow:0 1px 3px rgba(0,0,0,.35)}

/* bio */
.bio-frame{left:99px;top:600px;width:315px;height:351px;border:1px solid var(--line);padding:7px;background:var(--white);box-shadow:0 1px 4px rgba(0,0,0,.08)}
.bio-photo{width:100%;height:100%;background:linear-gradient(160deg,#e6c08a 0%,#b9875a 35%,#3a2d28 70%,#1e1a19 100%)}
.bio-actions{left:106px;top:890px;width:301px;height:54px;background:rgba(60,55,52,.72);color:var(--white);font-size:14px;font-weight:600;display:flex;align-items:center;justify-content:center;gap:12px}
.bio-title{left:450px;top:600px;width:670px;white-space:nowrap;font-family:"Cinzel",serif;font-weight:400;font-size:19px;line-height:26px;color:var(--ink)}
.bio-sub{left:450px;top:636px;font-size:13px;font-style:italic;color:var(--accent)}
.rec{left:452px;top:679px;display:flex;align-items:center;gap:6px;font-size:11px}
.rec .btn{background:var(--teal);color:var(--white);padding:2px 8px;border-radius:2px}
.rec .count{border:1px solid #999;padding:1px 6px;color:var(--ink)}
.rec .heart{color:var(--heart)}
.rec .likes{font-size:9px;color:var(--ink)}
.specialty{left:452px;top:703px;font-size:9px;color:var(--ink)}
.bio-text{left:450px;top:740px;width:668px;font-size:12px;line-height:25px;color:var(--body)}
.bio-text p+p{margin-top:25px}
.read-more{left:450px;top:942px;font-size:13px;font-weight:700;color:var(--accent)}

/* services */
.services{left:0;top:1005px;width:1200px;height:513px;background:var(--soft)}
.section-title{left:0;width:1200px;text-align:center;font-family:"Cinzel",serif;font-weight:400;font-size:26px;color:var(--ink);letter-spacing:1px}
.services-title{top:1046px}
.services-sub{left:0;top:1091px;width:1200px;text-align:center;font-size:16px;font-style:italic;color:var(--accent)}
.card{top:1141px;width:306px;height:329px;border:1px solid var(--line);padding:5px;background:var(--white)}
.card-photo{width:100%;height:100%}
.card-care{background:linear-gradient(160deg,#c9b9a8,#8e3d24 45%,#5a2516)}
.card-style{background:linear-gradient(160deg,#b7a897,#6a4a36 45%,#2f231d)}
.card-ext{background:linear-gradient(160deg,#cfd2d0,#3a2a22 45%,#1c1512)}
.card-label{left:6px;right:6px;top:233px;height:52px;background:rgba(55,50,48,.6);color:var(--white);font-weight:700;font-size:16px;display:flex;align-items:center;justify-content:center}

/* testimonials */
.testimonials{left:0;top:1518px;width:1200px;height:317px;background:var(--rose)}
.t-title{color:var(--white);top:1566px}
.quote-bg{left:99px;top:1620px;width:126px;height:126px;border-radius:50%;background:#ddd0c9}
.quote-mark{left:116px;top:1660px}
.avatar{left:176px;top:1622px;width:122px;height:122px;border-radius:50%;border:4px solid #e5d8d1;background:linear-gradient(150deg,#caa38a,#6b4b3a)}
.t-text{left:343px;top:1634px;width:770px;font-size:12.5px;line-height:29px;font-style:italic;color:var(--white)}
.t-name{left:340px;top:1728px;color:var(--white);font-family:"Cinzel",serif;font-size:19px}
.t-name span{font-family:"Open Sans",sans-serif;font-style:italic;font-size:12px;margin-left:8px}
.dots{left:0;top:1780px;width:1200px;display:flex;justify-content:center;gap:6px}
.dots i{width:13px;height:13px;border-radius:50%;background:var(--white)}
.dots i.on{background:var(--accent)}

/* booking */
.book-box{left:97px;top:1897px;width:1004px;height:286px;border:1px solid var(--line)}
.book-title{left:410px;top:1878px;width:380px;background:var(--white)}
.field{height:45px;border:1px solid #cfcac6;padding:0 14px;font-size:11px;color:#666;display:flex;align-items:center;background:var(--white)}
.field.msg{align-items:flex-start;padding-top:14px;height:92px}
.submit{left:426px;top:2149px;width:350px;height:52px;border-radius:3px;background:linear-gradient(180deg,#dbc3b7,var(--rose-deep));color:var(--white);font-weight:700;font-size:18px;display:flex;align-items:center;justify-content:center;letter-spacing:.5px}

/* connect */
.connect{left:0;top:2252px;width:1200px;height:191px;background:var(--cream)}
.connect-title{top:2280px}
.connect-sub{left:0;top:2326px;width:1200px;text-align:center;font-size:15px;color:var(--body)}
.social{left:0;top:2365px;width:1200px;display:flex;justify-content:center;gap:12px}
.social i{width:32px;height:32px;border-radius:50%;background:#cdb8ae}

/* footer */
.footer{left:0;top:2443px;width:1200px;height:166px;background:var(--footer)}
.footer-brand{left:0;top:2482px;width:1200px;text-align:center;color:var(--white);font-family:"Cinzel",serif;font-weight:700;font-size:19px}
.footer-links{left:0;top:2537px;width:1200px;text-align:center;font-size:12px;color:var(--white);word-spacing:6px}
.copyright{left:0;top:2561px;width:1200px;text-align:center;font-size:11px;color:var(--white)}
</style>
</head>
<body>

<section>
  <div class="abs hero" role="img" aria-label="Hero photograph of a woman with long voluminous curls"></div>
  <div class="abs hero-photo"></div>
  <header class="abs topbar"></header>
  <div class="abs brand">TRESS RADIANT<br><small>FROM ROOT TO SOUL</small></div>
  <div class="abs phone">
    <svg width="26" height="26" viewBox="0 0 26 26"><circle cx="13" cy="13" r="11.5" fill="none" stroke="#fff" stroke-width="2"/><path d="M9 7.5c1 0 1.5 2.5 1.5 3s-1 1-1 1.5c.5 1.5 2 3 3.5 3.5.5 0 1-1 1.5-1s3 .5 3 1.5c0 1.5-1.5 2.5-2.5 2.5C10.5 18.5 7.5 15.5 7.5 10c0-1 .5-2.5 1.5-2.5z" fill="#fff"/></svg>
    555-214-0370
  </div>
  <div class="abs login">
    <svg width="26" height="26" viewBox="0 0 26 26"><circle cx="13" cy="13" r="11.5" fill="none" stroke="#fff" stroke-width="2"/><circle cx="13" cy="10" r="3.5" fill="#fff"/><path d="M6.5 19c1-3.5 4-4.5 6.5-4.5s5.5 1 6.5 4.5z" fill="#fff"/></svg>
    LOGIN / SIGN UP
  </div>
  <nav class="abs nav">
    <span>HOME</span><span>BIO</span><span>SERVICES</span><span>PHOTO GALLERY</span><span>PAY DEPOSITS</span><span>LOCATION</span><span>CONTACT</span><span>FAQS</span>
  </nav>
  <h1 class="abs hero-title">TRESS RADIANT</h1>
  <div class="abs hero-sub">FROM ROOT TO SOUL</div>
  <svg class="abs arrow" style="left:34px" width="20" height="36" viewBox="0 0 20 36"><path d="M17 3 3 18l14 15" fill="none" stroke="#fff" stroke-opacity=".75" stroke-width="3"/></svg>
  <svg class="abs arrow" style="left:1146px" width="20" height="36" viewBox="0 0 20 36"><path d="M3 3l14 15L3 33" fill="none" stroke="#fff" stroke-opacity=".75" stroke-width="3"/></svg>
  <div class="abs tagline" style="left:116px">CREATIVE</div>
  <div class="abs tagline" style="left:452px">CLASSIC</div>
  <div class="abs tagline" style="left:786px">DISTINGUISHED</div>
</section>

<section>
  <div class="abs bio-frame"><div class="bio-photo" role="img" aria-label="Portrait of the stylist Marisol"></div></div>
  <div class="abs bio-actions">
    <svg width="16" height="12" viewBox="0 0 16 12"><rect width="16" height="12" rx="1" fill="#fff"/><path d="M0 1l8 6 8-6" fill="none" stroke="#555" stroke-width="1.4"/></svg>
    MESSAGE ME &nbsp;|&nbsp;
    <svg width="16" height="12" viewBox="0 0 16 12"><rect width="16" height="12" rx="1" fill="#fff"/><path d="M0 1l8 6 8-6" fill="none" stroke="#555" stroke-width="1.4"/></svg>
    CONTACT INFO
  </div>
  <h2 class="abs bio-title">TRESS RADIANT FROM ROOT TO SOUL BY MARISOL H.</h2>
  <div class="abs bio-sub">Stylist Tress R.R.S. By Marisol H. @ Lumen Salon Studios</div>
  <div class="abs rec"><span class="btn">♡ Recommend</span><span class="count">3</span><span class="heart">♥</span><span class="likes">59</span></div>
  <div class="abs specialty">Specialty: Extensions</div>
  <div class="abs bio-text">
    <p>Creative. Classic. Distinguished. These are just a few attributes that Marisol embodies. received in depth training from Brightwell Academy of Hair Design, where I had the opportunity to pair my experience with advanced technical training. My passion for art and design has given me the opportunity to express myself through hair design.</p>
    <p>I also stay abreast of current trends through industry events, hair shows, and continuing education so that I can offer my clients the best services in hair care, style, and extensions. I've spent the last five years perfecting my method of installing extensions which offers my clients a ...</p>
  </div>
  <div class="abs read-more">READ MORE &gt;&gt;</div>
</section>

<section>
  <div class="abs services"></div>
  <h2 class="abs section-title services-title">SERVICES</h2>
  <div class="abs services-sub">My passion for art and design has given me the opportunity to express myself through hair design</div>
  <div class="abs card" style="left:99px"><div class="card-photo card-care" role="img" aria-label="Client with long auburn hair"></div><div class="abs card-label">HAIR CARE</div></div>
  <div class="abs card" style="left:447px"><div class="card-photo card-style" role="img" aria-label="Styled brown curls"></div><div class="abs card-label">HAIR STYLE</div></div>
  <div class="abs card" style="left:795px"><div class="card-photo card-ext" role="img" aria-label="Client wearing curly extensions"></div><div class="abs card-label">EXTENSIONS</div></div>
</section>

<section>
  <div class="abs testimonials"></div>
  <h2 class="abs section-title t-title">TESTIMONIALS</h2>
  <div class="abs quote-bg"></div>
  <svg class="abs quote-mark" width="56" height="46" viewBox="0 0 56 46"><path d="M4 44V24C4 12 10 4 22 2v8c-6 2-8 6-8 12h8v22zM34 44V24c0-12 6-20 18-22v8c-6 2-8 6-8 12h8v22z" fill="#fff"/></svg>
  <div class="abs avatar" role="img" aria-label="Portrait of the reviewer"></div>
  <p class="abs t-text">It is a long established fact that a reader will be distracted by the readable content of a page when looking at its layout. The point of using Lorem Ipsum is that it has a more-or-less normal distribution of letters, as opposed to using 'Content here, content here', making it look like readable English.</p>
  <div class="abs t-name">Delphine Varga<span>(Varga Artistry in Portland, OR )</span></div>
  <div class="abs dots"><i class="on"></i><i></i><i></i></div>
</section>

<section>
  <div class="abs book-box"></div>
  <h2 class="abs section-title book-title">BOOK AN APPOINTMENT</h2>
  <div class="abs field" style="left:123px;top:1960px;width:301px">Name :</div>
  <div class="abs field" style="left:449px;top:1960px;width:301px">Email :</div>
  <div class="abs field" style="left:776px;top:1960px;width:301px">Phone Number :</div>
  <div class="abs field msg" style="left:123px;top:2033px;width:954px">Message :</div>
  <div class="abs submit">SUBMIT</div>
</section>

<section>
  <div class="abs connect"></div>
  <h2 class="abs section-title connect-title">STAY CONNECTED</h2>
  <div class="abs connect-sub">Keep up to date with changes and updates via our email newsletter.</div>
  <div class="abs social"><i></i><i></i><i></i><i></i><i></i></div>
</section>

<footer>
  <div class="abs footer"></div>
  <div class="abs footer-brand">TRESS RADIANT</div>
  <div class="abs footer-links">Home | Sitemap | Contact | Login</div>
  <div class="abs copyright">Copyright © 2016. Tress Radiant from root to soul. All Rights Reserved. Privacy Policy</div>
</footer>

</body>
</html>
```